Plumbing Company trying to attract new client base for particular works

In need of something to letterbox drop. There is an opportunity to provide "new sewer drains to the new sewer connections on your street".
There will be discounts for pensioners.
We have reviews from clients that are highly satisfied with our work.
Work booked within 1 months of stamped date on flyer will receive a further 10% off.
All work carried out by licences tradespeople.

LOGO will need to be altered to say "quillet plumbing" rather than contracting

Target Market(s)

Home owners in regional South Australia - age 30+

Industry/Entity Type

It Company

Requirements
Must have
• contact phone number, email, company name,
Nice to have
• images,

```html
<!DOCTYPE html>
<html lang="en">
<head>
<meta charset="utf-8">
<title>Quillet Plumbing – New Sewer Drains</title>
<link rel="stylesheet" href="https://fonts.googleapis.com/css2?family=Questrial&family=Montserrat:ital,wght@0,700;0,800;0,900;1,700&display=swap">
<style>
  :root {
    --yellow: #f6c619;
    --yellow-light: #fbe9a6;
    --black: #0d0d0d;
    --white: #ffffff;
    --grey: #8a8a8a;
    --soil: #8a5a3c;
    --gravel: #b9aea3;
  }
  html, body {
    margin: 0;
    padding: 0;
    overflow: hidden;
    background: var(--white);
  }
  .flyer {
    position: relative;
    width: 1200px;
    height: 848px;
    overflow: hidden;
    background: radial-gradient(ellipse 520px 360px at 430px 360px, var(--yellow-light) 0%, var(--yellow) 100%);
    font-family: "Montserrat", sans-serif;
    color: var(--black);
  }
  .shapes {
    position: absolute;
    inset: 0;
  }
  .headline {
    position: absolute;
    left: 38px;
    top: 16px;
    margin: 0;
    font-weight: normal;
  }
  .headline-intro {
    display: block;
    font-family: "Questrial", sans-serif;
    font-size: 52px;
    line-height: 64px;
    letter-spacing: -0.5px;
  }
  .headline-quote {
    display: block;
    font-family: "Montserrat", sans-serif;
    font-weight: 900;
    font-size: 55px;
    line-height: 64px;
    letter-spacing: 0.5px;
    text-shadow: 0 0 3px var(--white), 0 0 2px var(--white);
  }
  .benefits {
    position: absolute;
    left: 42px;
    top: 350px;
    margin: 0;
    font-weight: 800;
    font-size: 30px;
    line-height: 36px;
  }
  .offer {
    position: absolute;
    left: 42px;
    top: 497px;
    margin: 0;
    font-weight: 800;
    font-size: 30px;
    line-height: 44px;
  }
  .offer-second {
    display: block;
    padding-left: 156px;
  }
  .licence-band {
    position: absolute;
    left: 0;
    top: 602px;
    width: 1200px;
    height: 50px;
    background: var(--black);
  }
  .licence-text {
    position: absolute;
    right: 36px;
    top: 608px;
    margin: 0;
    color: var(--yellow);
    font-style: italic;
    font-weight: 700;
    font-size: 27px;
    line-height: 40px;
  }
  .footer {
    position: absolute;
    left: 0;
    top: 652px;
    width: 1200px;
    height: 196px;
    background: var(--white);
  }
  .brand-mark {
    position: absolute;
    left: 60px;
    top: 628px;
    width: 150px;
    height: 150px;
    background: var(--yellow);
    border: 6px solid var(--black);
    box-sizing: border-box;
  }
  .brand-name {
    position: absolute;
    left: 238px;
    top: 680px;
    margin: 0;
    font-weight: 800;
    font-size: 50px;
    line-height: 56px;
    letter-spacing: 1px;
    text-transform: uppercase;
    color: var(--black);
  }
  .brand-name span {
    display: block;
  }
  .call {
    position: absolute;
    left: 732px;
    top: 668px;
    margin: 0;
    font-weight: 900;
    font-size: 46px;
    line-height: 58px;
  }
  .call-number {
    display: block;
    font-size: 58px;
    line-height: 68px;
    letter-spacing: 2px;
  }
  .contact-line {
    position: absolute;
    left: 0;
    right: 36px;
    top: 794px;
    margin: 0;
    text-align: right;
    color: var(--grey);
    font-weight: 800;
    font-size: 27px;
    line-height: 40px;
  }
</style>
</head>
<body>
<main class="flyer">
  <svg class="shapes" width="1200" height="848" viewBox="0 0 1200 848" aria-hidden="false">
    <defs>
      <linearGradient id="trench-tones" x1="0" y1="0" x2="1" y2="0.3">
        <stop offset="0" stop-color="var(--gravel)"/>
        <stop offset="0.45" stop-color="#9c7055"/>
        <stop offset="1" stop-color="var(--soil)"/>
      </linearGradient>
    </defs>
    <polygon class="trench-photo" role="img" aria-label="Photo of an open trench with a new white sewer pipe laid in gravel and red soil"
      points="1045,0 1200,0 1200,602 1010,602 742,330" fill="url(#trench-tones)"/>
    <polyline class="trench-frame" points="1045,0 742,330 1010,602" fill="none" stroke="var(--black)" stroke-width="7"/>
  </svg>

  <h1 class="headline">
    <span class="headline-intro">There is an opportunity to provide</span>
    <span class="headline-quote">"new sewer drains to the</span>
    <span class="headline-quote">new sewer connections</span>
    <span class="headline-quote">on your street."</span>
  </h1>

  <p class="benefits">
    Discounts for pensioners.<br>
    We have reviews from clients that<br>
    are highly satisfied with our work.
  </p>

  <p class="offer">
    Work booked within 1 month of stamped date
    <span class="offer-second">on flyer will receive a further 10% off !</span>
  </p>

  <div class="licence-band"></div>
  <p class="licence-text">ALL WORK CARRIED OUT BY LICENSED TRADESPEOPLE.</p>

  <div class="footer"></div>
  <div class="brand-mark"></div>
  <p class="brand-name"><span>Quillet</span><span>Plumbing</span></p>

  <p class="call">Call us today on<span class="call-number">01632 960417</span></p>

  <p class="contact-line">enquiries@quilletplumbing.com • www.quilletplumbing.com</p>
</main>
</body>
</html>
```